Ferris Contracting LLC Business Card Design

I am looking for a creative and unique business card design. We are a commercial construction general contractor. With the name "FERRIS" Contracting, I am hoping to see some neat designs that correlate with the name.

```html
<!DOCTYPE html>
<html lang="en">
<head>
<meta charset="utf-8">
<title>Ferris Contracting LLC — Business Cards</title>
<link href="https://fonts.googleapis.com/css2?family=Roboto:wght@400;500;700;900&display=swap" rel="stylesheet">
<style>
  :root {
    --bg: #eeeff1;
    --blue-deep: #1a4f8f;
    --blue-mid: #2577c0;
    --blue-bright: #3ea2e6;
    --silver: #c3c7cc;
    --silver-light: #e2e4e7;
    --concrete-dark: #4a4b4d;
    --concrete: #69696b;
    --white: #ffffff;
    --ink-blue: #1c5a9c;
    --faint: #e9eaec;
  }
  * { box-sizing: border-box; margin: 0; padding: 0; }
  html, body { width: 1200px; height: 686px; overflow: hidden; }
  body {
    background: var(--bg);
    font-family: "Roboto", Arial, sans-serif;
    position: relative;
  }
  .card { position: absolute; overflow: hidden; }

  /* shared brand mark */
  .brand { display: flex; align-items: center; gap: 8px; position: absolute; }
  .brand__dot { width: 22px; height: 22px; border-radius: 50%; background: var(--silver); flex: none; }
  .brand__name {
    font-weight: 900; line-height: 1; letter-spacing: 1px;
    text-transform: uppercase;
  }

  /* card 1: owner front */
  .card--owner {
    left: 38px; top: 100px; width: 375px; height: 217px;
    background: linear-gradient(90deg, var(--blue-deep) 0%, var(--blue-mid) 45%, var(--silver) 100%);
  }
  .card--owner .brand { left: 24px; top: 90px; }
  .card--owner .brand__name { color: var(--blue-bright); font-size: 24px; }
  .card--owner .brand__sub { display:block; font-size: 10px; letter-spacing: 3px; margin-top: 3px; }
  .card--owner .person { position: absolute; left: 219px; top: 46px; color: var(--white); }
  .person__name { font-weight: 500; font-size: 19px; }
  .person__role { font-size: 13px; margin-top: 3px; opacity: .95; }
  .contacts { list-style: none; position: absolute; }
  .contacts li { display: flex; align-items: center; gap: 6px; font-size: 10.5px; margin-bottom: 5px; }
  .contacts svg { width: 11px; height: 11px; flex: none; }
  .card--owner .contacts { left: 219px; top: 111px; color: var(--white); }
  .card--owner .rule {
    position: absolute; left: 0; right: 0; top: 189px; height: 4px;
    background: linear-gradient(90deg, #9aa3ad, var(--silver-light));
  }

  /* card 2: brand back */
  .card--back {
    left: 38px; top: 379px; width: 375px; height: 212px;
    background: linear-gradient(180deg, #2f8fd4 0%, var(--blue-mid) 50%, var(--blue-deep) 100%);
  }
  .card--back .brand { left: 88px; top: 86px; }
  .card--back .brand__dot { width: 30px; height: 30px; }
  .card--back .brand__name { color: #4fb0ee; font-size: 32px; }
  .card--back .brand__sub { display:block; font-size: 13px; letter-spacing: 4px; margin-top: 4px; }

  /* card 3: vertical manager */
  .card--manager {
    left: 463px; top: 100px; width: 265px; height: 491px;
    background: radial-gradient(ellipse at 40% 30%, var(--concrete) 0%, var(--concrete-dark) 100%);
  }
  .card--manager .brand { left: 40px; top: 62px; }
  .card--manager .brand__name { color: var(--blue-bright); font-size: 26px; }
  .card--manager .brand__sub { display:block; font-size: 10px; letter-spacing: 3px; margin-top: 4px; }
  .card--manager .person { position: absolute; left: 0; right: 0; top: 222px; text-align: center; color: var(--white); }
  .card--manager .person__name { font-size: 20px; }
  .card--manager .person__role { font-size: 14px; }
  .card--manager .person__mail { font-size: 11.5px; margin-top: 3px; }

  /* card 4: white brand */
  .card--white {
    left: 781px; top: 100px; width: 380px; height: 217px;
    background: var(--white);
  }
  .card--white .brand { left: 90px; top: 84px; }
  .card--white .brand__dot { width: 30px; height: 30px; }
  .card--white .brand__name { color: var(--blue-mid); font-size: 32px; }
  .card--white .brand__sub { display:block; font-size: 13px; letter-spacing: 4px; margin-top: 4px; }

  /* card 5: contractor */
  .card--contractor {
    left: 781px; top: 379px; width: 380px; height: 212px;
    background: var(--white);
  }
  .card--contractor .band {
    position: absolute; left: 0; right: 0; top: 0; height: 70px;
    background: linear-gradient(180deg, #2a86cc, var(--blue-deep));
  }
  .card--contractor .stripe {
    position: absolute; top: 0; bottom: 0; left: 335px; width: 15px;
    background: linear-gradient(180deg, var(--blue-mid), var(--blue-deep));
  }
  .card--contractor .person { position: absolute; left: 37px; top: 17px; color: var(--white); }
  .card--contractor .person__name { font-weight: 700; font-size: 21px; }
  .card--contractor .contacts { left: 37px; top: 101px; color: var(--ink-blue); }
  .card--contractor .contacts li { margin-bottom: 10px; }
  .card--contractor .watermark {
    position: absolute; left: 0; top: 142px;
    font-weight: 900; font-size: 66px; color: var(--faint); letter-spacing: 2px;
  }
</style>
</head>
<body>

  <section class="card card--owner">
    <div class="brand"><span class="brand__dot"></span><span class="brand__name">Ferris<span class="brand__sub">Contracting</span></span></div>
    <div class="person">
      <p class="person__name">Dan Corley</p>
      <p class="person__role">Owner/Operator</p>
    </div>
    <ul class="contacts">
      <li><svg viewBox="0 0 12 12"><circle cx="6" cy="6" r="6" fill="#fff"/><path d="M3.8 3.2l1.2 1.2-.6.8c.5 1 1.2 1.7 2.2 2.2l.8-.6 1.2 1.2-.8.8C5.9 8.6 3.4 6.1 3.2 4z" fill="#2577c0"/></svg>: 555-210-3384</li>
      <li><svg viewBox="0 0 12 12"><circle cx="6" cy="6" r="6" fill="#fff"/><rect x="3" y="4" width="6" height="4" rx="1" fill="#2577c0"/></svg>: 555-214-7702</li>
      <li><svg viewBox="0 0 12 12"><circle cx="6" cy="6" r="6" fill="#fff"/><circle cx="6" cy="6" r="3" fill="none" stroke="#2577c0"/><path d="M3 6h6M6 3v6" stroke="#2577c0" stroke-width=".8"/></svg>www.ferriscontracting.com</li>
    </ul>
    <div class="rule"></div>
  </section>

  <section class="card card--back">
    <div class="brand"><span class="brand__dot"></span><span class="brand__name">Ferris<span class="brand__sub">Contracting</span></span></div>
  </section>

  <section class="card card--manager">
    <div class="brand"><span class="brand__dot"></span><span class="brand__name">Ferris<span class="brand__sub">Contracting</span></span></div>
    <div class="person">
      <p class="person__name">Rita Vance</p>
      <p class="person__role">Project Manager</p>
      <p class="person__mail">E: rita.vance@ferriscontracting.com</p>
    </div>
  </section>

  <section class="card card--white">
    <div class="brand"><span class="brand__dot"></span><span class="brand__name">Ferris<span class="brand__sub">Contracting</span></span></div>
  </section>

  <section class="card card--contractor">
    <div class="band"></div>
    <div class="watermark">FERRIS</div>
    <div class="stripe"></div>
    <div class="person">
      <p class="person__name">Owen Marsh</p>
      <p class="person__role">General Contractor</p>
    </div>
    <ul class="contacts">
      <li><svg viewBox="0 0 12 12"><circle cx="6" cy="6" r="6" fill="#1c5a9c"/><path d="M3.8 3.2l1.2 1.2-.6.8c.5 1 1.2 1.7 2.2 2.2l.8-.6 1.2 1.2-.8.8C5.9 8.6 3.4 6.1 3.2 4z" fill="#fff"/></svg>: 555-214-7702</li>
      <li><svg viewBox="0 0 12 12"><circle cx="6" cy="6" r="6" fill="#1c5a9c"/><rect x="3" y="4" width="6" height="4" rx="1" fill="#fff"/></svg>: 555-318-4496</li>
      <li><svg viewBox="0 0 12 12"><circle cx="6" cy="6" r="6" fill="#1c5a9c"/><circle cx="6" cy="6" r="3" fill="none" stroke="#fff"/><path d="M3 6h6M6 3v6" stroke="#fff" stroke-width=".8"/></svg>www.ferriscontracting.com</li>
    </ul>
  </section>

</body>
</html>
```